Podcast cover art (not a logo)

I’m launching an audio-only podcast for parents of neurodivergent children. The podcast is meant to feel like a calm, trusted professional voice — not a brand or a performance.

Style direction:
--Clean and minimal
--Calm and grounded
--Professional, not playful
--Nothing flashy, loud, or busy
--No cartoon imagery

Content on the cover:
--Podcast title: Under the Quiet Surface
--Subtitle or tagline: Supporting Neurodivergent Kids with Science, Not Shame (or Understanding Neurodivergent Kids)
--No episode numbers, no dates

Design preferences:
--Text-forward design
--Neutral or soft colors (muted blues, grays, off-whites)
--High contrast for readability at small sizes
--Simple, timeless font

What I do NOT want:
--A logo or branding system
--Illustrations of children or families
--Bright colors or playful graphics
--Trendy fonts or visual effects

Technical requirements:
--Square image
--3000 × 3000 pixels
--RGB color mode
--JPEG or PNG
--File size under 500 KB

Deliverables:
--Final cover art file
--Optional: one or two alternate background color versions

```html
<!DOCTYPE html>
<html lang="en">
<head>
<meta charset="utf-8">
<title>Under the Quiet Surface — Podcast Cover</title>
<link rel="stylesheet" href="https://fonts.googleapis.com/css2?family=IBM+Plex+Sans:wght@700&family=Source+Sans+3:wght@700;800&display=swap">
<style>
  :root {
    --navy: #1f3a54;
    --mist: #dce3ee;
    --white: #ffffff;
    --soft-white: #f1f1f1;
    --glow: #b3cde0;
    --steel: #5f87ad;
    --accent-bar: #35618a;
  }
  * { margin: 0; padding: 0; box-sizing: border-box; }
  html, body { width: 1200px; height: 1200px; overflow: hidden; background: var(--steel); }
  .cover {
    position: relative;
    width: 1200px;
    height: 1200px;
    overflow: hidden;
    background: radial-gradient(circle at 596px 680px, var(--glow) 0%, #8fb0cb 30%, #7096b9 55%, var(--steel) 80%);
  }
  .cover__shade {
    position: absolute;
    inset: 0;
  }
  .title-band {
    position: absolute;
    left: 0; top: 0;
    width: 1200px; height: 302px;
    background: var(--navy);
  }
  .title-band__word {
    position: absolute;
    left: 118px;
    top: 46px;
    font-family: "IBM Plex Sans", sans-serif;
    font-weight: 700;
    font-size: 238px;
    line-height: 1;
    letter-spacing: -4px;
    color: var(--white);
  }
  .subtitle-band {
    position: absolute;
    left: 0; top: 302px;
    width: 1200px; height: 146px;
    background: var(--mist);
  }
  .subtitle-band__words {
    position: absolute;
    left: 120px;
    top: 22px;
    font-family: "IBM Plex Sans", sans-serif;
    font-weight: 700;
    font-size: 112px;
    line-height: 1;
    letter-spacing: -1px;
    color: var(--navy);
  }
  .side-bar {
    position: absolute;
    left: 0; top: 780px;
    width: 59px; height: 338px;
    background: var(--accent-bar);
  }
  .tagline {
    position: absolute;
    left: 126px;
    top: 800px;
    font-family: "Source Sans 3", sans-serif;
    font-weight: 800;
    font-size: 80px;
    line-height: 97px;
    letter-spacing: -0.5px;
  }
  .tagline__line { display: block; color: var(--soft-white); }
  .tagline__line--dark { color: var(--navy); }
</style>
</head>
<body>
  <main class="cover">
    <svg class="cover__shade" width="1200" height="1200" viewBox="0 0 1200 1200" aria-hidden="true">
      <defs>
        <linearGradient id="band-fade" x1="0" y1="448" x2="0" y2="600" gradientUnits="userSpaceOnUse">
          <stop offset="0" stop-color="#1f3a54" stop-opacity="1"/>
          <stop offset="1" stop-color="#1f3a54" stop-opacity="0"/>
        </linearGradient>
      </defs>
      <polygon points="0,448 1200,448 620,600 0,600" fill="url(#band-fade)"/>
    </svg>

    <header class="title-band">
      <h1 class="title-band__word">Under</h1>
    </header>
    <div class="subtitle-band">
      <p class="subtitle-band__words">the Quiet Surface</p>
    </div>

    <div class="side-bar"></div>

    <p class="tagline">
      <span class="tagline__line">Supporting</span>
      <span class="tagline__line">Neurodivergent Kids</span>
      <span class="tagline__line tagline__line--dark">with Science, Not Shame</span>
    </p>
  </main>
</body>
</html>
```